Business card for massage therapy company called Brook Fern Wellness

Need business card for massage therapy company called Brook Fern Wellness. Would like my logo on the front and the back of the card I have 3 options of logos and you can play with what looks better.

Would like this information displayed on the back of the card:

Marcus Ellery
Licensed Massage Therapist
321-555-0147
brookfern-example.com
brookfern_rest_

```html
<!DOCTYPE html>
<html lang="en">
<head>
<meta charset="utf-8">
<title>Brook Fern Wellness – Business Card</title>
<link rel="stylesheet" href="https://fonts.googleapis.com/css2?family=Lora:wght@500&family=Josefin+Sans:wght@300;400&display=swap">
<style>
  :root {
    --backdrop: #efebe7;
    --card: #fbfaf8;
    --card-edge: #e4e0db;
    --sage: #5f6d57;
    --clay: #a67a63;
    --ink-soft: #6d6a64;
  }
  * { box-sizing: border-box; margin: 0; padding: 0; }
  html, body {
    width: 1200px; height: 1200px; overflow: hidden;
    background: var(--backdrop);
  }
  .sheet {
    position: relative; width: 1200px; height: 1200px;
  }
  .card {
    position: absolute; left: 220px;
    width: 760px; height: 434px;
    background: var(--card);
    border: 1px solid var(--card-edge);
    box-shadow: 0 10px 24px rgba(90, 80, 70, 0.12);
  }
  .card--front { top: 110px; display: flex; align-items: center; justify-content: center; }
  .card--back { top: 656px; }

  .brand-name {
    font-family: "Lora", serif;
    font-weight: 500;
    color: var(--sage);
    font-size: 62px;
    letter-spacing: 0.5px;
  }

  .monogram {
    position: absolute; left: 70px; top: 100px;
    width: 230px; height: 230px;
    border: 2px solid var(--sage);
    border-radius: 50%;
    display: flex; align-items: center; justify-content: center;
    text-align: center;
  }
  .monogram .brand-name { font-size: 30px; line-height: 1.2; width: 150px; }

  .details {
    position: absolute; left: 360px; top: 118px;
    font-family: "Josefin Sans", sans-serif;
    font-weight: 300;
    color: var(--sage);
  }
  .details__name {
    font-family: "Lora", serif; font-weight: 500;
    color: var(--clay); font-size: 38px; margin-bottom: 10px;
  }
  .details__title { font-size: 22px; color: var(--ink-soft); margin-bottom: 34px; }
  .details__line { font-size: 26px; font-weight: 400; margin-bottom: 16px; display: flex; align-items: center; gap: 10px; }
  .details__line svg { flex: none; }
</style>
</head>
<body>
  <main class="sheet">
    <section class="card card--front" aria-label="Card front">
      <p class="brand-name">Brook Fern Wellness</p>
    </section>

    <section class="card card--back" aria-label="Card back">
      <div class="monogram">
        <p class="brand-name">Brook Fern Wellness</p>
      </div>
      <div class="details">
        <p class="details__name">Marcus Ellery</p>
        <p class="details__title">Licensed Massage Therapist</p>
        <p class="details__line">321-555-0147</p>
        <p class="details__line">brookfern-example.com</p>
        <p class="details__line">
          <svg width="22" height="22" viewBox="0 0 22 22" aria-hidden="true">
            <circle cx="11" cy="11" r="9" fill="none" stroke="#a67a63" stroke-width="2"/>
          </svg>
          brookfern_rest_
        </p>
      </div>
    </section>
  </main>
</body>
</html>
```